inspirational business card

I want to use the Vector on Pixavend.com (number 58172046) and I will purchase the vector to send it to the designer once the general concept is approved. You can download it for free for a one time use on providing a design for this request.
Within the vector, insert:
Tessa Brundle
Guidance and Partnering

I prefer a vertical card but do not require vertical.

Contact info:

Tessa Brundle, J.D.
Collaborative Lawyer
Certified Divorce Coach
Mediation Coach
PHONE 515/555-0143
EMAIL: tbjd@quellmail.net

Website: Guidanceandpartnering.com
Settlementcourse.com

I like greens, blue and grey. I do not want black font, and would like the font to be legible without needing perfect reading vision (no super small font).
I would like the overall theme to convey growth and nurturance.
I like the vector I selected because of the growth and light portrayed.
Not too frilly or too bold. I would like to to appeal to both sexes.

Target Market(s)

Generally professional women 35-60

Industry/Entity Type

Attorney

Font styles to use
Serif
Sans Serif

Colors
acd136
cadf82
fbf289
9d9d9d

Requirements
Must have
• My project does not need to have my photo but you could use it if you want
Nice to have
• Vertical
• I like rounded edges on the cards
Should not have
• I do not like my name appearing two times in close proximity. I'm not a flowery person.

```html
<!DOCTYPE html>
<html lang="en">
<head>
<meta charset="utf-8">
<title>Business Card – Tessa Brundle</title>
<link href="https://fonts.googleapis.com/css2?family=Cormorant+Garamond:wght@500;600&family=Lato:wght@400;700&display=swap" rel="stylesheet">
<style>
  :root {
    --stage: #414141;
    --card-light: #f8f9c8;
    --card-mid: #e6efa6;
    --card-edge: #c9dc86;
    --leaf-dark: #4f9a1c;
    --leaf-mid: #7cc02c;
    --leaf-light: #b6dc5a;
    --brand-green: #6d8f3e;
    --text-grey: #6b6b5e;
    --label-green: #5c7a32;
  }
  * { margin: 0; padding: 0; box-sizing: border-box; }
  html, body {
    width: 1200px; height: 1000px; overflow: hidden;
    background: var(--stage);
  }
  .stage {
    width: 1200px; height: 1000px;
    display: flex; flex-direction: column;
    align-items: center; justify-content: center; gap: 60px;
  }
  .card {
    position: relative;
    width: 720px; height: 410px;
    border-radius: 18px;
    overflow: hidden;
    background: radial-gradient(ellipse at 45% 50%, var(--card-light) 0%, var(--card-mid) 55%, var(--card-edge) 100%);
  }
  .card__vine {
    position: absolute; top: 0; right: 0;
    width: 300px; height: 410px;
  }
  .brand {
    position: absolute;
    width: 250px;
    display: flex; flex-direction: column; align-items: center;
  }
  .brand__circle {
    width: 110px; height: 110px; border-radius: 50%;
    background: var(--brand-green);
    margin-bottom: 16px;
  }
  .brand__name {
    font-family: "Cormorant Garamond", serif;
    font-weight: 600; font-size: 30px; letter-spacing: 1px;
    color: var(--text-grey);
    line-height: 1; white-space: nowrap;
  }
  .brand__tagline {
    font-family: "Cormorant Garamond", serif;
    font-weight: 600; font-size: 12px; letter-spacing: 3px;
    color: var(--text-grey);
    margin-top: 6px; white-space: nowrap;
  }
  .card--front .brand { left: 200px; top: 110px; }
  .card--back .brand { left: 25px; top: 110px; }
  .contact {
    position: absolute; left: 300px; top: 110px;
    font-family: "Lato", sans-serif; color: var(--text-grey);
  }
  .contact__name {
    font-size: 30px; font-weight: 700; color: var(--brand-green);
    line-height: 1.1; white-space: nowrap;
  }
  .contact__role { font-size: 17px; margin: 6px 0 28px; }
  .contact__row { font-size: 15px; margin-bottom: 10px; display: flex; gap: 12px; white-space: nowrap; }
  .contact__label { font-weight: 700; color: var(--label-green); width: 60px; }
</style>
</head>
<body>
<main class="stage">
  <section class="card card--front">
    <svg class="card__vine" viewBox="0 0 300 410" role="img" aria-label="Green leaves along a curved vine in the card corner">
      <defs>
        <linearGradient id="vineFront" x1="0" y1="0" x2="1" y2="1">
          <stop offset="0" stop-color="var(--leaf-light)"/>
          <stop offset="0.5" stop-color="var(--leaf-mid)"/>
          <stop offset="1" stop-color="var(--leaf-dark)"/>
        </linearGradient>
      </defs>
      <path d="M60 0 C150 30 200 120 210 230 C220 320 260 380 300 410 L300 0 Z" fill="url(#vineFront)" opacity="0.9"/>
    </svg>
    <div class="brand">
      <div class="brand__circle"></div>
      <span class="brand__name">COMPANY NAME</span>
      <span class="brand__tagline">YOUR TAGLINE</span>
    </div>
  </section>

  <section class="card card--back">
    <svg class="card__vine" viewBox="0 0 300 410" role="img" aria-label="Green leaves along a curved vine in the card corner">
      <defs>
        <linearGradient id="vineBack" x1="0" y1="0" x2="1" y2="1">
          <stop offset="0" stop-color="var(--leaf-light)"/>
          <stop offset="0.5" stop-color="var(--leaf-mid)"/>
          <stop offset="1" stop-color="var(--leaf-dark)"/>
        </linearGradient>
      </defs>
      <path d="M110 0 C180 30 220 120 230 230 C240 320 268 380 300 410 L300 0 Z" fill="url(#vineBack)" opacity="0.9"/>
    </svg>
    <div class="brand">
      <div class="brand__circle"></div>
      <span class="brand__name">COMPANY NAME</span>
      <span class="brand__tagline">YOUR TAGLINE</span>
    </div>
    <div class="contact">
      <h1 class="contact__name">Tessa Brundle, J.D.</h1>
      <p class="contact__role">Collaborative Lawyer</p>
      <p class="contact__row"><span class="contact__label">PHONE:</span><span>515/555-0143</span></p>
      <p class="contact__row"><span class="contact__label">EMAIL:</span><span>tbjd@quellmail.net</span></p>
      <p class="contact__row"><span class="contact__label">SITE:</span><span>Guidanceandpartnering.com</span></p>
    </div>
  </section>
</main>
</body>
</html>
```